Business Card Design for Consulting Company

I require a Business Card design for my Consulting company. <br/><br/>My company name is: Marek Olvani Consulting Inc.<br/>My website is: www.marekolvaniconsulting.example<br/><br/>My company focuses on management and software development for the Tallobrix CRM platform (www.tallobrix.example)<br/><br/>I have a logo already designed...see attached.
Updates

Also Include my Name and Title: Marek T.L. Olvani President

Target Market(s)

Tallobrix Customers

Contact Information for Business Card

Only include my LOGO (provided)
My Name: Marek TL Olvani
My Title: President
My Company Name: Marek Olvani Consulting Inc.
My Website: www.marekolvaniconsulting.example
My Email: marek.olvani.consulting@mailbox.example

NO PHONE NUMBER
NO ADDRESS

Font styles to use
Serif
Sans Serif
Other font styles liked:
• see my website: www.marekolvaniconsulting.example

Colors

Designer to choose colors to be used in the design.

Requirements
Must have
• Must include my Orange
• Include my name (Marek T.L. Olvani), title (President) company name, website and email
• It should also have a tag line like: Tallobrix Consulting
• I'm flexible with the tag line
Should not have
• Don't include my phone number or address

```html
<!DOCTYPE html>
<html lang="en">
<head>
<meta charset="utf-8">
<title>Marek Olvani Consulting Inc. – Business Card</title>
<link rel="stylesheet" href="https://fonts.googleapis.com/css2?family=Exo+2:wght@400;700&display=swap">
<style>
  :root {
    --bg: #eceeef;
    --card-white: #ffffff;
    --panel-dark: #232b35;
    --band-black: #1e1d1f;
    --accent-yellow: #fdc010;
    --accent-orange: #ff8b00;
    --accent-pale: #fedd80;
    --text-light: #ffffff;
  }
  html, body {
    margin: 0;
    width: 1200px;
    height: 800px;
    overflow: hidden;
    background: var(--bg);
  }
  .canvas {
    width: 1200px;
    height: 800px;
    display: flex;
    align-items: center;
    justify-content: center;
  }
  .business-card {
    width: 1000px;
    height: 553px;
    display: block;
    box-shadow: 0 10px 30px rgba(0,0,0,0.15);
  }
  .card-text { font-family: "Exo 2", sans-serif; }
  .holder-name { font-weight: 700; font-size: 31px; fill: var(--accent-yellow); }
  .company-name { font-weight: 400; font-size: 20px; fill: var(--text-light); }
  .contact-line { font-weight: 400; font-size: 19px; fill: var(--text-light); }
  .brand-name { font-weight: 700; font-size: 46px; fill: var(--accent-orange); }
</style>
</head>
<body>
<main class="canvas">
  <svg class="business-card" viewBox="0 0 700 387" xmlns="http://www.w3.org/2000/svg" aria-label="Business card for Marek Olvani Consulting Inc.">
    <rect class="card-base" width="700" height="387" fill="var(--card-white)"/>

    <!-- Accent stripes -->
    <polygon class="stripe-yellow" points="302,0 336,0 298,387 145,387" fill="var(--accent-yellow)"/>
    <polygon class="stripe-pale" points="290,95 298,95 298,387 180,387" fill="var(--accent-pale)"/>
    <polygon class="stripe-orange" points="293,100 298,100 298,387 222,387" fill="var(--accent-orange)"/>

    <!-- Dark information panel -->
    <polygon class="info-panel" points="336,0 700,0 700,387 298,387 298,95 317,50" fill="var(--panel-dark)"/>

    <!-- Name band -->
    <polygon class="name-band" points="262,50 685,50 685,95 243,95" fill="var(--band-black)"/>
    <rect class="edge-bar" x="685" y="0" width="15" height="125" fill="var(--accent-yellow)"/>

    <!-- Brand name in place of mark -->
    <text class="card-text brand-name" x="28" y="203">Olvani</text>

    <!-- Card text -->
    <text class="card-text holder-name" x="508" y="82" text-anchor="middle">Marek Olvani</text>
    <text class="card-text company-name" x="498" y="206" text-anchor="middle">Marek Olvani Consulting Inc.</text>
    <text class="card-text contact-line" x="685" y="315" text-anchor="end" textLength="370" lengthAdjust="spacingAndGlyphs">marek.olvani.consulting@mailbox.example</text>
    <text class="card-text contact-line" x="685" y="357" text-anchor="end" textLength="345" lengthAdjust="spacingAndGlyphs">www.marekolvaniconsulting.example</text>
  </svg>
</main>
</body>
</html>
```